Music Festival Business Cards

The Lantern Gathering
Produced by Bramblewood Sound Collective LLC
New music festival in Arkansas.

Target Market(s)

18-35 year olds

Industry/Entity Type

Festival

Contact Information for Business Card

We are a 5-partner team producing a music festival in Arkansas. We need slick business cards, and I want them to be square.

Requirements
Must have
• I NEED THESE TO BE IN SQUARE SIZE - 2x2 or 2.5x2.5... please not regular size.
• I need www.lanternmeet.example as the link to website.

```html
<!DOCTYPE html>
<html lang="en">
<head>
<meta charset="UTF-8">
<title>The Lantern Gathering — Business Cards</title>
<link href="https://fonts.googleapis.com/css2?family=Lato:wght@400;700&display=swap" rel="stylesheet">
<style>
  :root {
    --backdrop: #5f5f5f;
    --teal: #36cbd3;
    --white: #ffffff;
    --ink: #050505;
  }
  * { margin: 0; padding: 0; box-sizing: border-box; }
  html, body {
    width: 1200px;
    height: 900px;
    overflow: hidden;
    background: var(--backdrop);
    font-family: "Lato", sans-serif;
  }
  .stage { position: relative; width: 1200px; height: 900px; }
  .card {
    position: absolute;
    top: 259px;
    width: 392px;
    height: 393px;
    overflow: hidden;
  }
  .card--front { left: 197px; background: var(--teal); }
  .card--back { left: 614px; background: var(--ink); }

  .front-accent {
    position: absolute;
    left: 300px;
    top: 26px;
    width: 190px;
    height: 190px;
    background: var(--white);
  }

  .holder {
    position: absolute;
    left: 36px;
    top: 190px;
    color: var(--white);
  }
  .holder__name {
    font-size: 23px;
    font-weight: 400;
    letter-spacing: 0.3px;
    line-height: 1;
  }
  .holder__role {
    margin-top: 10px;
    font-size: 14.5px;
    letter-spacing: 0.2px;
    line-height: 1;
  }

  .contact-list {
    position: absolute;
    left: 36px;
    top: 267px;
    list-style: none;
    color: var(--white);
  }
  .contact-list__item {
    display: flex;
    align-items: center;
    height: 23.5px;
    font-size: 17px;
  }
  .contact-list__icon {
    width: 14px;
    height: 14px;
    margin-right: 11px;
    fill: var(--white);
  }

  .brand {
    position: absolute;
    left: 0;
    right: 0;
    top: 174px;
    display: flex;
    flex-direction: column;
    align-items: center;
  }
  .brand__mark {
    width: 22px;
    height: 22px;
    background: var(--teal);
    margin-bottom: 22px;
  }
  .brand__name {
    color: var(--teal);
    font-size: 23px;
    font-weight: 700;
    letter-spacing: 2.5px;
    white-space: nowrap;
  }
</style>
</head>
<body>
<main class="stage">
  <section class="card card--front" aria-label="Business card front">
    <div class="front-accent" aria-hidden="true"></div>
    <div class="holder">
      <p class="holder__name">MARCUS HALE</p>
      <p class="holder__role">MANAGING DIRECTOR</p>
    </div>
    <ul class="contact-list">
      <li class="contact-list__item">
        <svg class="contact-list__icon" viewBox="0 0 14 14" aria-hidden="true"><path d="M1 4c0-2 2-3 6-3s6 1 6 3v1H10V3.5H4V5H1z"/><rect x="2" y="6" width="10" height="7" rx="1"/></svg>
        044-555 010 201
      </li>
      <li class="contact-list__item">
        <svg class="contact-list__icon" viewBox="0 0 14 14" aria-hidden="true"><path d="M4 0h6a1 1 0 0 1 1 1v12a1 1 0 0 1-1 1H4a1 1 0 0 1-1-1V1a1 1 0 0 1 1-1zm0.5 1.5v9.5h5V1.5z"/></svg>
        034-555 010 202
      </li>
      <li class="contact-list__item">
        <svg class="contact-list__icon" viewBox="0 0 14 14" aria-hidden="true"><path d="M1 3h12v1L7 8 1 4zM1 5.2l6 4 6-4V11H1z"/></svg>
        info@lanternmeet.example
      </li>
      <li class="contact-list__item">
        <svg class="contact-list__icon" viewBox="0 0 14 14" aria-hidden="true"><path d="M7 1a6 6 0 1 0 0 12A6 6 0 0 0 7 1zm-1 2.5 2 1-1 2 2 1v2l-2 2-1-2-2-1 1-2-2-1z"/></svg>
        www.lanternmeet.example
      </li>
    </ul>
  </section>

  <section class="card card--back" aria-label="Business card back">
    <div class="brand">
      <div class="brand__mark" aria-hidden="true"></div>
      <p class="brand__name">THE LANTERN GATHERING</p>
    </div>
  </section>
</main>
</body>
</html>
```